Locksmith SmartPhone Web Design Project

I am a locksmith and focus on customers that use their smart phones to find me. I have a static web page that I created myself but it is horrible. See for yourself at www.tarvelmacks.com.au

I want a cross-platform static site that simply shows the information and with the ability to change minor items like pricing. I want it to be compelling in its look and feel (not overwhelming) but simple. It must have a; click to call button; the ability to install a hit counter from zorbiqly.com; payment information just like the current graphic of card/cash/quenzo (lumo/brevindale only).

This will be hosted on my own server.
Updates

Hello Designers,

I have updated the brief in the must have and nice to have fields.

Thank you all,

Toby.

Hello to all Designers,

There is about 9 days left before the deadline. The overall level of competition is extremely high and I would like to thank all the designers who have submitted so far, 27 submissions in total so far. Excellent work.

If you have submitted already and wish to provide new designs, I am keen to see them. 

Hi guys, time is almost up. Please submit any new designs that you may have. The quality has been excellent so far.

Toby.

Target Market(s)

People who are locked out of their house/shop/office etc.

Industry/Entity Type

Locksmith

Requirements
Must have
• click to call button
hit counter from zorbiqly
payment graphic card/cash/quenzo (lumo/brevindale only)
cross platform compatibility smartphone/phablet
Single column page preferable, can have two columns.
Nice to have
• When the page loads regardless of the mobile device, all info should be presented. In other words no vertical or horizontal scroll bars.
Should not have
• hidden code, advertising, credits etc

```html
<!DOCTYPE html>
<html lang="en">
<head>
<meta charset="utf-8">
<title>Tarvelmacks Locksmiths – Lockout Service</title>
<link rel="stylesheet" href="https://fonts.googleapis.com/css2?family=Oswald:wght@300;400;500&display=swap">
<style>
  :root {
    --page-bg: #f4f4f4;
    --panel-bg: #ffffff;
    --brand-orange: #d1512a;
    --brand-grey: #5c5d62;
    --text-dark: #45464a;
    --text-mid: #5a5b5f;
    --text-soft: #6a6b6f;
    --call-green-top: #86c20a;
    --call-green-bottom: #5f9e00;
    --call-border: #a9d86a;
    --pay-bg: #f1f2f4;
    --pay-mark: #b9bcc2;
  }
  * { box-sizing: border-box; margin: 0; padding: 0; }
  html, body {
    width: 1200px;
    height: 1000px;
    overflow: hidden;
    background: var(--page-bg);
    font-family: "Oswald", "Arial Narrow", sans-serif;
  }
  .site {
    position: absolute;
    left: 280px;
    top: 20px;
    width: 640px;
    height: 960px;
    background: var(--panel-bg);
    text-align: center;
    box-shadow: 0 2px 10px rgba(0,0,0,0.08);
  }
  .top-bar {
    height: 16px;
    background: var(--brand-orange);
  }
  .brand {
    margin-top: 50px;
    display: flex;
    flex-direction: column;
    align-items: center;
  }
  .brand-mark {
    width: 236px;
    height: 236px;
    border-radius: 50%;
    background: var(--brand-grey);
  }
  .brand-name {
    margin-top: 26px;
    font-weight: 500;
    font-size: 40px;
    line-height: 46px;
    color: var(--brand-orange);
    text-transform: lowercase;
  }
  .service-title {
    margin-top: 20px;
    font-weight: 300;
    font-size: 52px;
    line-height: 64px;
    color: var(--text-dark);
  }
  .service-offer {
    margin-top: 6px;
    font-weight: 300;
    font-size: 33px;
    line-height: 44px;
    color: var(--text-mid);
  }
  .call-button {
    display: block;
    width: 376px;
    height: 80px;
    margin: 26px auto 0;
    border: 2px solid var(--call-border);
    border-radius: 6px;
    background: linear-gradient(var(--call-green-top), var(--call-green-bottom));
    color: #fff;
    font-weight: 300;
    font-size: 46px;
    line-height: 74px;
    letter-spacing: 2px;
    text-decoration: none;
    word-spacing: 10px;
  }
  .payments {
    margin-top: 50px;
    display: flex;
    justify-content: center;
    gap: 32px;
  }
  .payment {
    width: 128px;
    height: 90px;
    background: var(--pay-bg);
    border-radius: 4px;
    display: flex;
    align-items: center;
    justify-content: center;
    gap: 6px;
    font-weight: 400;
    font-size: 20px;
    color: var(--text-mid);
  }
  .payment-mark {
    width: 12px;
    height: 12px;
    background: var(--pay-mark);
  }
  .business-details {
    margin-top: 46px;
    font-weight: 300;
    font-size: 21px;
    color: var(--text-soft);
    word-spacing: 2px;
  }
  .business-details span + span { margin-left: 14px; }
</style>
</head>
<body>
  <main class="site">
    <div class="top-bar"></div>

    <header class="brand">
      <div class="brand-mark"></div>
      <p class="brand-name">tarvelmacks<br>locksmiths</p>
    </header>

    <h1 class="service-title">Locksmith Lockout Service</h1>
    <p class="service-offer">Locked Out? $150 Gets You In. EASY!</p>

    <a class="call-button" href="tel:0400218736">0400 218 736</a>

    <section class="payments" aria-label="Accepted payments">
      <div class="payment"><span class="payment-mark"></span>Lumo</div>
      <div class="payment"><span class="payment-mark"></span>Brevindale</div>
      <div class="payment"><span class="payment-mark"></span>Quenzo</div>
    </section>

    <footer class="business-details">
      <span>ABN: 51027384916</span>
      <span>Master Licence: 382640175</span>
      <span>Visits: 1947</span>
    </footer>
  </main>
</body>
</html>
```